KEM Logistics - Banner 2.5' x 8' for 20+ locations

Need a banner designed that will pop. This banner will be displayed at over 20 of our transportation facilities. Goal is for the banner to grab the attention of employees, contractors and clients and help reinforce our mission and core values. Designed needs to include KEM Logo, our core values and mission statement. Red and Black are the main company colors and we need to stay within that theme and color pallet. Attached is a previous version that was too basic and boring. Willing to consider a design that excludes the mission statement.

```html
<!DOCTYPE html>
<html lang="en">
<head>
<meta charset="utf-8">
<title>KEM Logistics – Core Values Banner</title>
<link rel="stylesheet" href="https://fonts.googleapis.com/css2?family=Barlow+Condensed:wght@500;600;700&display=swap">
<style>
  :root {
    --stage: #494949;
    --red: #d0230f;
    --black: #1c1a19;
    --white: #ffffff;
    --paper-light: #ffffff;
    --paper-grey: #d9d9d9;
    --photo-dark: #b43c1c;
    --photo-light: #e2703a;
  }
  * { box-sizing: border-box; margin: 0; padding: 0; }
  html, body {
    width: 1200px; height: 509px; overflow: hidden;
    background: var(--stage);
    font-family: "Barlow Condensed", "Arial Narrow", sans-serif;
  }
  .banner {
    position: absolute; left: 53px; top: 79px;
    width: 1094px; height: 342px; overflow: hidden;
    background:
      linear-gradient(115deg, transparent 55%, rgba(180,180,180,.35) 75%, transparent 95%),
      linear-gradient(90deg, var(--paper-light) 0%, #f4f4f4 35%, var(--paper-grey) 70%, #ececec 100%);
  }
  .brand {
    position: absolute; left: 40px; top: 140px;
    font-weight: 700; font-size: 48px; line-height: 1;
    color: var(--red); letter-spacing: 1px;
  }
  .value {
    position: absolute; width: 144px; height: 163px;
  }
  .value svg.hex { position: absolute; inset: 0; }
  .value .icon {
    position: absolute; left: 50%; top: 47px; transform: translate(-50%, -50%);
  }
  .value .label {
    position: absolute; left: 0; right: 0;
    text-align: center; color: var(--white);
    font-weight: 500; font-size: 17px; line-height: 22px;
  }
  .value--red .label { top: 80px; }
  .value--black .label { top: 83px; }
  .value--black .label.single { top: 92px; }

  .mission-disc { position: absolute; left: 811px; top: -87px; width: 516px; height: 516px; border-radius: 50%; background: var(--black); }
  .mission-photo {
    position: absolute; left: 841px; top: -57px; width: 456px; height: 456px; border-radius: 50%;
    background: radial-gradient(circle at 70% 45%, var(--photo-light), var(--photo-dark) 80%);
  }
  .mission-arc { position: absolute; left: 0; top: 0; }
  .mission {
    position: absolute; left: 913px; top: 86px; width: 180px;
    color: var(--white); font-weight: 500; font-size: 19px; line-height: 27.2px;
  }
  .quote-mark {
    position: absolute; left: 913px; top: 287px; width: 160px; height: 30px;
    display: flex; align-items: center; justify-content: space-between;
  }
  .quote-mark .rule { width: 45px; height: 3px; background: var(--white); }
  .quote-mark .glyph { color: var(--black); font-weight: 700; font-size: 62px; line-height: 1; margin-top: 26px; }
</style>
</head>
<body>
<main class="banner">
  <div class="brand">KEM Logistics</div>

  <!-- Core values: red row -->
  <section class="value value--red" style="left:343px;top:27px">
    <svg class="hex" viewBox="-6 -6 156 175" width="144" height="163" preserveAspectRatio="none"><polygon points="72,0 144,41 144,122 72,163 0,122 0,41" fill="var(--red)" stroke="var(--red)" stroke-width="12" stroke-linejoin="round"/></svg>
    <svg class="icon" width="44" height="50" viewBox="0 0 44 50" fill="var(--white)">
      <rect x="2" y="24" width="8" height="24" rx="1.5"/>
      <path d="M13 25 L21 12 Q24 8 26 12 L25 22 L38 22 Q43 23 41 28 L38 44 Q37 48 32 48 L13 48 Z"/>
      <rect x="22" y="0" width="2.5" height="6" rx="1"/><rect x="29" y="3" width="2.5" height="6" rx="1" transform="rotate(35 30 6)"/><rect x="14" y="3" width="2.5" height="6" rx="1" transform="rotate(-35 15 6)"/>
    </svg>
    <p class="label">Do the right things<br>for the right reasons</p>
  </section>
  <section class="value value--red" style="left:503px;top:27px">
    <svg class="hex" viewBox="-6 -6 156 175" width="144" height="163" preserveAspectRatio="none"><polygon points="72,0 144,41 144,122 72,163 0,122 0,41" fill="var(--red)" stroke="var(--red)" stroke-width="12" stroke-linejoin="round"/></svg>
    <svg class="icon" width="54" height="56" viewBox="0 0 54 56" fill="var(--white)">
      <path d="M8 0 L14 8 L10 8 L10 22 L6 22 L6 8 L2 8 Z"/><path d="M46 0 L52 8 L48 8 L48 22 L44 22 L44 8 L40 8 Z"/>
      <path d="M4 24 L9 31 L6 31 L6 46 L2 46 L2 31 L-1 31 Z"/><path d="M50 24 L55 31 L52 31 L52 46 L48 46 L48 31 L45 31 Z"/>
      <rect x="17" y="34" width="20" height="6"/><rect x="13" y="41" width="28" height="6"/><rect x="10" y="48" width="34" height="7"/>
      <rect x="21" y="24" width="12" height="9" rx="3"/><circle cx="27" cy="18" r="4.5"/>
    </svg>
    <p class="label">Pursue growth<br>and development</p>
  </section>
  <section class="value value--red" style="left:659px;top:27px">
    <svg class="hex" viewBox="-6 -6 156 175" width="144" height="163" preserveAspectRatio="none"><polygon points="72,0 144,41 144,122 72,163 0,122 0,41" fill="var(--red)" stroke="var(--red)" stroke-width="12" stroke-linejoin="round"/></svg>
    <svg class="icon" width="54" height="46" viewBox="0 0 54 46" fill="var(--white)">
      <circle cx="11" cy="14" r="6"/><circle cx="43" cy="14" r="6"/><circle cx="27" cy="9" r="8"/>
      <path d="M0 44 L0 32 Q0 22 11 22 Q16 22 18 25 L18 44 Z"/><path d="M54 44 L54 32 Q54 22 43 22 Q38 22 36 25 L36 44 Z"/>
      <path d="M15 44 L15 30 Q15 19 27 19 Q39 19 39 30 L39 44 Z"/>
    </svg>
    <p class="label">Build a positive<br>team atmosphere</p>
  </section>

  <!-- Core values: black row -->
  <section class="value value--black" style="left:270px;top:161px">
    <svg class="hex" viewBox="-6 -6 156 175" width="144" height="163" preserveAspectRatio="none"><polygon points="72,0 144,41 144,122 72,163 0,122 0,41" fill="var(--black)" stroke="var(--black)" stroke-width="12" stroke-linejoin="round"/></svg>
    <svg class="icon" width="46" height="46" viewBox="0 0 46 46" fill="var(--white)">
      <rect x="0" y="10" width="46" height="9" rx="1"/><rect x="3" y="21" width="40" height="25" rx="1"/>
      <rect x="20" y="10" width="6" height="36" fill="var(--black)"/>
      <path d="M23 10 Q14 -2 9 3 Q6 9 23 10 Z M23 10 Q32 -2 37 3 Q40 9 23 10 Z"/>
    </svg>
    <p class="label">Deliver WOW<br>through service</p>
  </section>
  <section class="value value--black" style="left:426px;top:161px">
    <svg class="hex" viewBox="-6 -6 156 175" width="144" height="163" preserveAspectRatio="none"><polygon points="72,0 144,41 144,122 72,163 0,122 0,41" fill="var(--black)" stroke="var(--black)" stroke-width="12" stroke-linejoin="round"/></svg>
    <svg class="icon" width="40" height="46" viewBox="0 0 40 46">
      <path d="M20 1 L38 8 L38 22 Q38 38 20 45 Q2 38 2 22 L2 8 Z" fill="var(--white)"/>
      <path d="M11 23 L18 30 L30 16" fill="none" stroke="var(--black)" stroke-width="4.5" stroke-linecap="round" stroke-linejoin="round"/>
    </svg>
    <p class="label">Do everything<br>safely</p>
  </section>
  <section class="value value--black" style="left:583px;top:161px">
    <svg class="hex" viewBox="-6 -6 156 175" width="144" height="163" preserveAspectRatio="none"><polygon points="72,0 144,41 144,122 72,163 0,122 0,41" fill="var(--black)" stroke="var(--black)" stroke-width="12" stroke-linejoin="round"/></svg>
    <svg class="icon" width="50" height="50" viewBox="0 0 50 50"><circle cx="25" cy="25" r="25" fill="var(--white)"/></svg>
    <p class="label single">Have fun</p>
  </section>

  <!-- Mission -->
  <div class="mission-disc"></div>
  <div class="mission-photo" role="img" aria-label="Warehouse worker in an orange shirt moving boxes on a hand truck, tinted orange"></div>
  <svg class="mission-arc" width="1094" height="342" viewBox="0 0 1094 342">
    <path d="M869 150 Q900 20 1094 30" fill="none" stroke="var(--white)" stroke-width="7" stroke-linecap="round"/>
  </svg>
  <p class="mission">Provide the best customer experience while creating an environment of growth and opportunity for our customers, employees, and service providers.</p>
  <div class="quote-mark"><span class="rule"></span><span class="glyph">”</span><span class="rule"></span></div>
</main>
</body>
</html>
```